Salon and Spa Distributor Business Card

Need a business card. We are are distributor in the salon and spa industry. We identify with natural beauty. Need a card with:
Company Name: Petal Haven"
Title: "President & CEO"
Address
Company Phone number
email
website
Tag Line:" The Professional Salon Source"

Industry/Entity Type

Business

Contact Information for Business Card

Name: Lena Morcott
Title: "President & CEO"
Address: 317 Birchfield Ln, Oakvane, NJ 07481
Company Phone number: 800-463-9152
email: lenamorcott@petalhaven-example.com
website: www.petalhaven-example.com

Requirements
Should not have
• No black backgrounds

```html
<!DOCTYPE html>
<html lang="en">
<head>
<meta charset="utf-8">
<title>Petal Haven – Business Card</title>
<link href="https://fonts.googleapis.com/css2?family=Questrial&family=Tinos:ital,wght@1,400;1,700&display=swap" rel="stylesheet">
<style>
  :root {
    --green-deep: #0b6b38;
    --green-mid: #3f9a44;
    --green-light: #6cbf47;
    --green-text: #3a9a3f;
    --ink: #111111;
    --paper: #ffffff;
    --stage: #ececec;
  }
  * { margin: 0; padding: 0; box-sizing: border-box; }
  html, body {
    width: 1200px; height: 586px; overflow: hidden;
    background: var(--stage);
  }
  .canvas { position: relative; width: 1200px; height: 586px; }

  .card {
    position: absolute; top: 129px;
    width: 502px; height: 301px;
    overflow: hidden;
  }

  /* Front */
  .card-front {
    left: 61px;
    background: linear-gradient(90deg, var(--green-deep) 0%, var(--green-mid) 28%, var(--green-light) 50%, var(--green-mid) 72%, var(--green-deep) 100%);
  }
  .front-brand {
    position: absolute; left: 0; right: 0; top: 110px;
    display: flex; justify-content: center; align-items: center; gap: 12px;
    font-family: "Questrial", sans-serif; font-size: 36px; color: var(--paper);
  }
  .front-brand .brand-dot {
    width: 22px; height: 22px; border-radius: 50%; background: var(--paper);
  }
  .front-website {
    position: absolute; left: 0; right: 0; top: 238px;
    display: flex; justify-content: center; align-items: center; gap: 6px;
    font-family: "Questrial", sans-serif; font-size: 13px; color: var(--paper);
  }
  .front-website .rule { width: 58px; height: 1.5px; background: var(--paper); }
  .tagline {
    position: absolute; left: 0; right: 0; top: 263px; text-align: center;
    font-family: "Tinos", serif; font-style: italic; font-weight: 700;
    font-size: 12px; letter-spacing: 4.2px; color: var(--ink);
  }

  /* Back */
  .card-back { left: 619px; background: var(--paper); }
  .back-brand {
    position: absolute; right: 24px; top: 54px;
    display: flex; align-items: center; gap: 10px;
    font-family: "Questrial", sans-serif; font-size: 27px; color: var(--green-text);
  }
  .back-brand .brand-dot {
    width: 20px; height: 20px; border-radius: 50%; background: var(--green-text);
  }
  .person-name {
    position: absolute; left: 29px; top: 137px;
    font-family: "Questrial", sans-serif; font-size: 17px; color: var(--green-text);
  }
  .person-title {
    position: absolute; left: 29px; top: 161px;
    font-family: "Tinos", serif; font-style: italic; font-size: 11.5px; color: var(--ink);
  }
  .contact-list { position: absolute; left: 28px; top: 203px; list-style: none; }
  .contact-list li {
    display: flex; align-items: center; gap: 7px; height: 24px;
    font-family: "Questrial", sans-serif; font-size: 12px; color: var(--ink);
  }
  .contact-list svg { width: 17px; height: 17px; flex: none; }
  .back-band {
    position: absolute; left: 0; right: 0; bottom: 0; height: 13px;
    background: linear-gradient(90deg, var(--green-deep) 0%, var(--green-light) 50%, var(--green-deep) 100%);
  }
</style>
</head>
<body>
<main class="canvas">

  <section class="card card-front" aria-label="Card front">
    <div class="front-brand"><span class="brand-dot"></span><span>Petal Haven</span></div>
    <div class="front-website"><span class="rule"></span><span>www.petalhaven-example.com</span><span class="rule"></span></div>
    <p class="tagline">The Professional Salon Source</p>
  </section>

  <section class="card card-back" aria-label="Card back">
    <div class="back-brand"><span class="brand-dot"></span><span>Petal Haven</span></div>
    <p class="person-name">Lena Morcott</p>
    <p class="person-title">President &amp; CEO</p>
    <ul class="contact-list">
      <li>
        <svg viewBox="0 0 20 20" aria-hidden="true"><circle cx="10" cy="10" r="10" fill="#3a9a3f"/><path d="M5.5 8.5c0-1.5 2-2.5 4.5-2.5s4.5 1 4.5 2.5l-1.6.6-.5-1.2h-4.8l-.5 1.2zM7 10h6l1 4H6z" fill="#fff"/></svg>
        <span>800-463-9152</span>
      </li>
      <li>
        <svg viewBox="0 0 20 20" aria-hidden="true"><circle cx="10" cy="10" r="10" fill="#3a9a3f"/><rect x="5" y="6.5" width="10" height="7" fill="none" stroke="#fff" stroke-width="1.3"/><path d="M5 6.5l5 4 5-4" fill="none" stroke="#fff" stroke-width="1.3"/></svg>
        <span>lenamorcott@petalhaven-example.com</span>
      </li>
      <li>
        <svg viewBox="0 0 20 20" aria-hidden="true"><circle cx="10" cy="10" r="10" fill="#3a9a3f"/><path d="M10 4a4 4 0 0 0-4 4c0 3 4 8 4 8s4-5 4-8a4 4 0 0 0-4-4z" fill="#fff"/><circle cx="10" cy="8" r="1.6" fill="#3a9a3f"/></svg>
        <span>317 Birchfield Ln, Oakvane, NJ 07481</span>
      </li>
    </ul>
    <div class="back-band"></div>
  </section>

</main>
</body>
</html>
```